I need a header for the web site www.harlowspipeworks.example/demo
It must include the following
Existig Logo (I will upload the .png)
Text: Serving Calgary and Surrounding Areas for Over 30 Years!
24 Hour Service
Call 403.718.2946 (Note this isn't the actual phone number I will need to be able to change the Phone number once the site is ready to put in a tracking number so I am hoping I get a PSD file with this where the text is editable)
We wnat the feel to be warm and geared more towards a residential customer rather than an industial customer.
We would like blue tones but are open to anything warm.

Size: Aprroximately 960x300

• Rounded Corners to match the content area on the site

```html
<!DOCTYPE html>
<html lang="en">
<head>
<meta charset="utf-8">
<title>Harlow's Pipeworks – Header</title>
<link rel="stylesheet" href="https://fonts.googleapis.com/css2?family=Roboto+Condensed:wght@400;700&family=Open+Sans:wght@400;700&family=Kreon:wght@300;400&display=swap">
<style>
  :root {
    --page-bg: #ffffff;
    --tile-light: #dff2f5;
    --tile-mid: #c4e1e6;
    --tile-deep: #a9cbd2;
    --band-top: #6e9fd6;
    --band-bottom: #3866a6;
    --navy: #28318c;
    --red: #d3202f;
    --ink: #2e2e2e;
    --white: #ffffff;
    --site-bg: #7f9fa4;
    --site-bar: #2d4c59;
    --card: #fbfbfb;
    --nav-ink: #3a3a3a;
    --rule: #e3e3e3;
    --slide-top: #a08468;
    --slide-bottom: #7a6350;
    --caption-bg: rgba(30, 28, 26, 0.72);
    --gold: #e7b15a;
  }
  * { box-sizing: border-box; margin: 0; padding: 0; }
  html, body { width: 960px; height: 1200px; overflow: hidden; background: var(--page-bg); }
  body { position: relative; font-family: "Open Sans", Arial, sans-serif; }

  /* ---------- Header banner ---------- */
  .banner {
    position: absolute; width: 921px; height: 283px;
    border-radius: 14px; overflow: hidden;
  }
  .banner--hero { left: 21px; top: 95px; }
  .banner--site {
    left: 45px; top: 64px;
    transform: scale(0.7752, 0.8127); transform-origin: 0 0;
    border: 2.5px solid #111; border-radius: 16px;
  }
  .banner__scene {
    position: absolute; inset: 0;
    background: linear-gradient(160deg, var(--tile-light) 0%, var(--tile-mid) 55%, var(--tile-deep) 100%);
  }
  .banner__name {
    position: absolute; left: 115px; top: 44px;
    font-family: "Roboto Condensed", Arial, sans-serif; font-weight: 700;
    font-size: 26px; letter-spacing: 2px; color: var(--ink); white-space: nowrap;
  }
  .banner__icon { position: absolute; }
  .banner__icon--clock { left: 576px; top: 112px; }
  .banner__icon--phone { left: 458px; top: 163px; }
  .banner__hours, .banner__call {
    position: absolute; right: 20px; white-space: nowrap;
    font-family: "Roboto Condensed", Arial, sans-serif; font-weight: 700; line-height: 1;
  }
  .banner__hours { top: 126px; font-size: 47px; color: var(--navy); }
  .banner__call { top: 180px; font-size: 49px; color: var(--red); }
  .banner__band {
    position: absolute; left: 0; right: 0; bottom: 0; height: 45px;
    background: linear-gradient(var(--band-top), var(--band-bottom));
    display: flex; align-items: center; justify-content: center;
    font-family: "Roboto Condensed", Arial, sans-serif; font-weight: 700;
    font-size: 32px; color: var(--white); white-space: nowrap;
  }
  .banner__screw { position: absolute; top: 12px; }
  .banner__screw--left { left: 10px; }
  .banner__screw--right { right: 4px; }

  /* ---------- Site preview ---------- */
  .site {
    position: absolute; left: 83px; top: 433px; width: 797px; height: 739px;
    background: var(--site-bg); overflow: hidden;
  }
  .site__topbar {
    position: absolute; left: 0; top: 0; width: 100%; height: 45px;
    background: var(--site-bar); border-bottom: 1px dashed #9ab3b8;
  }
  .site__search {
    position: absolute; left: 602px; top: 17px; width: 122px; height: 19px;
    border-radius: 4px; background: #1f3844; border: 1px solid #4c6873;
    font-size: 8px; color: #8ea6ad; padding: 3px 8px;
  }
  .site__search svg { position: absolute; right: 6px; top: 4px; }
  .site__card {
    position: absolute; left: 51px; top: 303px; width: 708px; height: 450px;
    background: var(--card); border-radius: 8px 8px 0 0;
  }
  .site__nav { display: flex; height: 47px; padding-left: 22px; border-bottom: 1px solid var(--rule); }
  .site__nav-item {
    font-size: 9px; font-weight: 700; color: var(--nav-ink);
    display: flex; align-items: center; padding: 0 13px;
    border-right: 1px solid var(--rule); white-space: nowrap;
  }
  .site__slide {
    position: absolute; left: 0; top: 47px; width: 708px; height: 250px;
    background: linear-gradient(180deg, var(--slide-top), var(--slide-bottom));
  }
  .site__caption {
    position: absolute; left: 377px; top: 30px; width: 292px; height: 194px;
    background: var(--caption-bg); border-radius: 8px; padding: 18px 22px; color: #e6e2dc;
  }
  .site__meta { font-size: 8px; color: #9d968c; font-style: italic; }
  .site__meta b { color: var(--white); }
  .site__caption-title { font-family: "Kreon", Georgia, serif; font-weight: 300; font-size: 21px; color: var(--white); margin: 4px 0 6px; }
  .site__caption-text { font-size: 8.2px; line-height: 13.5px; color: #cfc9c0; }
  .site__more { position: absolute; right: 12px; bottom: 4px; font-size: 8.5px; color: var(--gold); }
  .site__pointer {
    position: absolute; left: 216px; top: 290px; width: 0; height: 0;
    border-left: 8px solid transparent; border-right: 8px solid transparent;
    border-bottom: 8px solid var(--card);
  }
  .site__arrow {
    position: absolute; top: 457px; width: 50px; height: 50px; border-radius: 50%;
    background: var(--white); display: flex; align-items: center;
  }
  .site__arrow--prev { left: 28px; padding-left: 8px; }
  .site__arrow--next { left: 739px; padding-left: 10px; }
  .site__thumbs { position: absolute; left: 18px; top: 313px; display: flex; gap: 16px; }
  .site__thumb { width: 70px; height: 40px; border: 1px solid #999; }
  .site__thumb--active { box-shadow: 0 2px 5px rgba(0,0,0,0.5); }
  .site__headings {
    position: absolute; left: 0; top: 374px; width: 708px; height: 31px;
    background: #f0f0f0; display: flex; font-size: 8.5px; font-weight: 700; color: #333;
  }
  .site__heading { display: flex; align-items: center; justify-content: center; }
  .site__heading--articles { width: 469px; border-right: 1px solid var(--rule); }
  .site__heading--company { flex: 1; }
  .site__article-thumb { position: absolute; left: 29px; top: 430px; width: 96px; height: 30px; border: 1px solid #888; background: #eee; }
  .site__article-title { position: absolute; left: 146px; top: 429px; font-family: "Kreon", Georgia, serif; font-size: 16px; color: #333; }
  .site__address { position: absolute; left: 502px; top: 428px; font-size: 8.5px; color: #333; }
</style>
</head>
<body>

  <header class="banner banner--hero">
    <div class="banner__scene" role="img" aria-label="Bright modern bathroom with a white toilet and wall cabinet"></div>
    <div class="banner__name">HARLOW'S PIPEWORKS</div>
    <svg class="banner__icon banner__icon--clock" width="68" height="68" viewBox="0 0 68 68" aria-hidden="true">
      <circle cx="34" cy="34" r="31" fill="#f4f4f8" stroke="#6a6fb8" stroke-width="5"/>
      <circle cx="34" cy="34" r="24" fill="#fff" stroke="#c9cbe0"/>
      <line x1="34" y1="34" x2="34" y2="15" stroke="#28318c" stroke-width="3"/>
      <line x1="34" y1="34" x2="50" y2="38" stroke="#d3202f" stroke-width="2.5"/>
      <circle cx="34" cy="34" r="2.5" fill="#28318c"/>
    </svg>
    <svg class="banner__icon banner__icon--phone" width="70" height="74" viewBox="0 0 70 74" aria-hidden="true">
      <path d="M14 8 C4 14 2 30 10 46 C18 62 34 72 50 70 L58 58 L44 48 L36 56 C28 52 22 42 20 32 L30 26 L24 6 Z" fill="#8a8e96" stroke="#d3202f" stroke-width="3"/>
      <circle cx="28" cy="38" r="2.5" fill="#fff"/><circle cx="34" cy="44" r="2.5" fill="#fff"/><circle cx="22" cy="32" r="2.5" fill="#fff"/>
    </svg>
    <div class="banner__hours">24hr Service</div>
    <div class="banner__call">Call 403.718.2946</div>
    <div class="banner__band">
      <svg class="banner__screw banner__screw--left" width="20" height="20" viewBox="0 0 20 20" aria-hidden="true"><circle cx="10" cy="10" r="9" fill="#3a4f74"/><path d="M5 5 L15 15 M15 5 L5 15" stroke="#8da0c0" stroke-width="2"/></svg>
      Serving Calgary and Surrounding Areas for Over 30 Years!
      <svg class="banner__screw banner__screw--right" width="20" height="20" viewBox="0 0 20 20" aria-hidden="true"><circle cx="10" cy="10" r="9" fill="#3a4f74"/><path d="M5 5 L15 15 M15 5 L5 15" stroke="#8da0c0" stroke-width="2"/></svg>
    </div>
  </header>

  <section class="site" aria-label="Header shown in the site layout">
    <div class="site__topbar">
      <div class="site__search">search this site...
        <svg width="10" height="10" viewBox="0 0 10 10" aria-hidden="true"><circle cx="4" cy="4" r="3" fill="none" stroke="#9ab" stroke-width="1.4"/><line x1="6" y1="6" x2="9" y2="9" stroke="#9ab" stroke-width="1.6"/></svg>
      </div>
    </div>

    <div class="site__arrow site__arrow--prev"><svg width="10" height="14" viewBox="0 0 10 14" aria-hidden="true"><path d="M8 1 L2 7 L8 13" fill="none" stroke="#888" stroke-width="2"/></svg></div>
    <div class="site__arrow site__arrow--next"><svg width="10" height="14" viewBox="0 0 10 14" aria-hidden="true"><path d="M2 1 L8 7 L2 13" fill="none" stroke="#888" stroke-width="2"/></svg></div>

    <div class="site__card">
      <nav class="site__nav">
        <span class="site__nav-item">HOME</span>
        <span class="site__nav-item">SERVICES »</span>
        <span class="site__nav-item">PRODUCT REVIEWS</span>
        <span class="site__nav-item">LINKS</span>
        <span class="site__nav-item">ARTICLES</span>
        <span class="site__nav-item">CONTACT US</span>
        <span class="site__nav-item">ABOUT US</span>
        <span class="site__nav-item">EMPLOYEE LOGIN</span>
      </nav>
      <div class="site__slide" role="img" aria-label="Photo of radiant floor heating tubing laid across a gravel subfloor">
        <div class="site__caption">
          <p class="site__meta">Posted by <b>admin</b> on Sep 2010</p>
          <h2 class="site__caption-title">Industrial Plumbing</h2>
          <p class="site__caption-text">Donec nec facilisis nisi. Vivamus tempor feugiat velit gravida vehicula. Donec faucibus pellentesque ipsum id varius. Ut rutrum metus sed neque ultricies a dictum ante sagittis. Proin in facilisis diam. Sed placerat imperdiet purus, id sollicitudin magna pretium sit amet. Vivamus orci dolor, iaculis at volutpat eget, fermentum vel quam. Nullam non neque urna, ut ultrices nisi. Nulla convallis aliquam...</p>
          <span class="site__more">Read More</span>
        </div>
      </div>
      <div class="site__pointer"></div>
      <div class="site__thumbs">
        <div class="site__thumb" style="background:#f4f4f4" role="img" aria-label="Line sketch thumbnail"></div>
        <div class="site__thumb" style="background:linear-gradient(#8a5a3c,#d9d4cc)" role="img" aria-label="Freestanding bathtub"></div>
        <div class="site__thumb site__thumb--active" style="background:linear-gradient(#b59b80,#a8764e)" role="img" aria-label="Floor heating tubing"></div>
        <div class="site__thumb" style="background:linear-gradient(#9aa3a8,#5e6a70)" role="img" aria-label="Boiler room"></div>
        <div class="site__thumb" style="background:linear-gradient(#b6b0a6,#6b645c)" role="img" aria-label="Mechanical room piping"></div>
        <div class="site__thumb" style="background:linear-gradient(#7d7668,#3f4a40)" role="img" aria-label="Glass vessel sink"></div>
        <div class="site__thumb" style="background:linear-gradient(#d8d8d8,#4a4a4a)" role="img" aria-label="Stone vessel basin"></div>
        <div class="site__thumb" style="background:linear-gradient(#6a4a36,#c8b8a4)" role="img" aria-label="Bathroom vanity with window"></div>
      </div>
      <div class="site__headings">
        <div class="site__heading site__heading--articles">MOST RECENT ARTICLES</div>
        <div class="site__heading site__heading--company">HARLOW'S PIPEWORKS</div>
      </div>
      <div class="site__article-thumb" role="img" aria-label="Article thumbnail"></div>
      <div class="site__article-title">Toilet Rebates</div>
      <div class="site__address">Mailing Address:</div>
    </div>

    <header class="banner banner--site">
      <div class="banner__scene" role="img" aria-label="Bright modern bathroom with a white toilet and wall cabinet"></div>
      <div class="banner__name">HARLOW'S PIPEWORKS</div>
      <svg class="banner__icon banner__icon--clock" width="68" height="68" viewBox="0 0 68 68" aria-hidden="true">
        <circle cx="34" cy="34" r="31" fill="#f4f4f8" stroke="#6a6fb8" stroke-width="5"/>
        <circle cx="34" cy="34" r="24" fill="#fff" stroke="#c9cbe0"/>
        <line x1="34" y1="34" x2="34" y2="15" stroke="#28318c" stroke-width="3"/>
        <line x1="34" y1="34" x2="50" y2="38" stroke="#d3202f" stroke-width="2.5"/>
        <circle cx="34" cy="34" r="2.5" fill="#28318c"/>
      </svg>
      <svg class="banner__icon banner__icon--phone" width="70" height="74" viewBox="0 0 70 74" aria-hidden="true">
        <path d="M14 8 C4 14 2 30 10 46 C18 62 34 72 50 70 L58 58 L44 48 L36 56 C28 52 22 42 20 32 L30 26 L24 6 Z" fill="#8a8e96" stroke="#d3202f" stroke-width="3"/>
        <circle cx="28" cy="38" r="2.5" fill="#fff"/><circle cx="34" cy="44" r="2.5" fill="#fff"/><circle cx="22" cy="32" r="2.5" fill="#fff"/>
      </svg>
      <div class="banner__hours">24hr Service</div>
      <div class="banner__call">Call 403.718.2946</div>
      <div class="banner__band">
        <svg class="banner__screw banner__screw--left" width="20" height="20" viewBox="0 0 20 20" aria-hidden="true"><circle cx="10" cy="10" r="9" fill="#3a4f74"/><path d="M5 5 L15 15 M15 5 L5 15" stroke="#8da0c0" stroke-width="2"/></svg>
        Serving Calgary and Surrounding Areas for Over 30 Years!
        <svg class="banner__screw banner__screw--right" width="20" height="20" viewBox="0 0 20 20" aria-hidden="true"><circle cx="10" cy="10" r="9" fill="#3a4f74"/><path d="M5 5 L15 15 M15 5 L5 15" stroke="#8da0c0" stroke-width="2"/></svg>
      </div>
    </header>
  </section>

</body>
</html>
```